New web Design for TELMOnet

Need a web design for our company TELMOnet, Inc. We are an IT services company providing our services to State/Local governments, federal government and commercial clients. Please take a look at our existing website (www.telmonet.com) to know more about our offerings and services. Our website should reflect our services that we provide primarily to state/local and federal governments in the USA and the website should be a responsive and compatible to view it over the web from a PC, tablet or a smart phone with the ability of a CMS.

Reason: We are currently reviewing additional designs. Please submit more asap. Thank you for all your help

Reason: Looking for more design

Reason: Looking for more designs

```html
<!DOCTYPE html>
<html lang="en">
<head>
<meta charset="utf-8">
<title>TELMOnet, Inc. — Public Sector Technology</title>
<link href="https://fonts.googleapis.com/css2?family=Questrial&family=Open+Sans:wght@400;600&display=swap" rel="stylesheet">
<style>
:root{
  --navy:#0d1b4f;
  --navy-2:#1b2d6e;
  --sky:#5fb2ea;
  --sky-2:#8dd0f6;
  --red:#e23b3b;
  --ink:#1d2a5c;
  --text:#555;
  --muted:#8a8a8a;
  --line:#e2e2e2;
  --band:#f2f2f4;
  --foot:#22397f;
  --foot-2:#1b2f6c;
  --foot-bar:#2a3564;
}
*{margin:0;padding:0;box-sizing:border-box}
html,body{width:858px;height:1200px;overflow:hidden;background:#fff}
body{position:relative;font-family:"Open Sans",sans-serif;color:var(--text)}
.abs{position:absolute}

.topbar{left:0;top:0;width:858px;height:70px;background:linear-gradient(180deg,var(--navy) 0%,var(--navy-2) 100%)}
.brand{left:90px;top:18px;display:flex;align-items:center;gap:6px}
.brand-mark{width:12px;height:12px;border-radius:50%;background:#fff}
.brand-name{font-family:"Questrial",sans-serif;font-size:22px;color:#fff;line-height:1}
.brand-tag{left:92px;top:46px;font-size:7px;color:#9fb4e6}
.util-links{right:108px;top:9px;font-size:8.5px;color:#d6def5}
.util-links span{margin:0 4px}

.mainnav{left:0;top:70px;width:858px;height:35px;background:linear-gradient(180deg,var(--sky) 0%,var(--sky-2) 100%);display:flex;justify-content:center;align-items:center}
.mainnav a{font-family:"Questrial",sans-serif;color:#fff;font-size:11px;text-decoration:none;padding:0 16px;border-left:1px solid rgba(255,255,255,.45);line-height:14px}
.mainnav a:first-child{border-left:0}

.hero{left:0;top:105px;width:858px;height:346px;background:linear-gradient(180deg,#4fa7e0 0%,#a9d6f2 38%,#e9e4da 62%,#cfc6b8 100%)}
.hero-card{left:230px;top:115px;width:376px;height:108px;background:rgba(226,45,45,.9);text-align:center;color:#fff;padding-top:14px}
.hero-kicker{font-family:"Questrial",sans-serif;font-size:14.5px;letter-spacing:.2px}
.hero-title{font-family:"Questrial",sans-serif;font-size:26px;line-height:30px;margin-top:2px}
.hero-sub{font-size:8.2px;line-height:14.5px;margin-top:3px}
.hero-dots{left:406px;top:329px;display:flex;gap:3px}
.hero-dots i{width:8px;height:8px;border-radius:50%;background:#fff;display:block}

.service{top:474px;width:150px;text-align:center}
.service svg{display:block;margin:0 auto;height:42px}
.service h3{font-family:"Questrial",sans-serif;font-weight:400;font-size:15px;color:var(--ink);margin-top:15px}
.service p{font-size:7.6px;line-height:13.5px;color:var(--muted);margin-top:4px}
.service .more{display:block;font-size:7.8px;color:var(--red);font-weight:600;margin-top:4px}

.divider{left:109px;top:614px;width:646px;height:1px;background:var(--line)}

.what{left:116px;top:640px;width:340px}
.what h2{font-family:"Questrial",sans-serif;font-weight:400;font-size:15px;color:#222}
.what .lead{font-size:9.8px;line-height:15px;color:#444;margin-top:9px}
.what .body{font-size:7.8px;line-height:15.3px;color:var(--muted);margin-top:7px}
.what .label{font-size:8px;font-weight:600;color:#333;margin-top:5px}
.products{display:flex;gap:14px;margin-top:8px;align-items:center}
.products span{font-family:"Questrial",sans-serif;font-size:17px;font-weight:400}
.p1{color:#e89a1f}.p2{color:#3f9b3a}.p3{color:#2b6cc2}.p4{color:#33b06a}

.recent{left:500px;top:642px;width:270px}
.recent h2{font-family:"Questrial",sans-serif;font-weight:400;font-size:15px;color:var(--ink)}
.project{position:absolute;left:0;display:flex;gap:7px}
.project .thumb{width:52px;height:41px;flex:none}
.project h4{font-family:"Questrial",sans-serif;font-weight:400;font-size:10.3px;color:#333}
.project p{font-size:7.5px;line-height:14px;color:var(--muted);margin-top:2px}

.certs{left:0;top:864px;width:858px;height:62px;background:var(--band)}
.row-label{font-family:"Questrial",sans-serif;font-size:13.5px;color:#666}
.badge{position:absolute;border:1px solid #ccc}

.clients{left:0;top:926px;width:858px;height:74px}
.client{position:absolute;display:flex;align-items:center;gap:4px;font-family:"Questrial",sans-serif;color:#333;white-space:nowrap}

.footer{left:0;top:1000px;width:858px;height:162px;background:linear-gradient(180deg,var(--foot) 0%,var(--foot-2) 100%)}
.fcol{position:absolute;top:29px}
.fcol h5{font-family:"Questrial",sans-serif;font-weight:400;font-size:12px;color:#fff}
.fcol ul{list-style:none;margin-top:6px}
.fcol li{font-size:8.3px;color:#c9d3ef;line-height:17.7px;padding-left:2px}
.social{display:flex;gap:3px;margin-top:4px}
.social i{display:block;width:17px;height:17px;border-radius:50%;background:#fff}
.legal{left:0;top:1162px;width:858px;height:38px;background:var(--foot-bar);font-size:8px;color:#a9b1d0;padding:11px 0 0 128px}
</style>
</head>
<body>

<header class="abs topbar">
  <div class="abs brand"><span class="brand-mark"></span><span class="brand-name">TELMOnet</span></div>
  <div class="abs brand-tag">Public Sector Technology</div>
  <nav class="abs util-links">Home<span>|</span>Clients<span>|</span>Career<span>|</span>Contact Us</nav>
</header>

<nav class="abs mainnav">
  <a>HARBOR-E</a><a>SOLUTIONS</a><a>PRODUCTS</a><a>ABOUT US</a><a>ALLIANCES</a><a>MEDIA</a><a>CONTRACT VEHICLES</a>
</nav>

<section class="abs hero" role="img" aria-label="Photograph of a domed government capitol building under a blue sky with a flag">
  <div class="abs hero-card">
    <div class="hero-kicker">SUSPENDISSE QUAM LEO MOLESTIE</div>
    <div class="hero-title">PROVIDING IT SERVICES</div>
    <div class="hero-sub">Libero a tempus libero lectus feugiat felis Morbi diam mauris viverra in gravida<br>eu mattis in ante Morbi eget arcu Morbi</div>
  </div>
  <div class="abs hero-dots"><i></i><i></i><i></i><i></i></div>
</section>

<section class="abs service" style="left:113px">
  <svg viewBox="0 0 44 42" fill="none" stroke="#e23b3b" stroke-width="2.2"><rect x="3" y="3" width="38" height="27" rx="2"/><path d="M16 37h12M22 30v7"/><circle cx="14" cy="17" r="5"/><path d="M14 12v5h5"/><path d="M24 24v-6M29 24v-9M34 24v-12" stroke-width="3"/></svg>
  <h3>IT Planning</h3>
  <p>Praesent sit amet est In dictum dolor<br>eu dictum porttitor enim felis</p>
  <span class="more">LEARN MORE</span>
</section>
<section class="abs service" style="left:275px">
  <svg viewBox="0 0 52 42" fill="none" stroke="#e23b3b" stroke-width="2.2"><circle cx="22" cy="10" r="6"/><circle cx="22" cy="10" r="2"/><circle cx="9" cy="22" r="4.5"/><path d="M20 18h26v18H20zM16 39h34"/></svg>
  <h3>Systems Integration</h3>
  <p>Praesent sit amet est In dictum dolor<br>eu dictum porttitor enim felis</p>
  <span class="more">LEARN MORE</span>
</section>
<section class="abs service" style="left:437px">
  <svg viewBox="0 0 44 42"><circle cx="22" cy="21" r="17" fill="#e23b3b"/><path d="M8 16c9 2 19 1 28-6M10 30c8-6 16-7 26-2M20 5c-2 11 0 23 6 33" stroke="#fff" stroke-width="2.2" fill="none"/></svg>
  <h3>Network Services</h3>
  <p>Praesent sit amet est In dictum dolor<br>eu dictum porttitor enim felis</p>
  <span class="more">LEARN MORE</span>
</section>
<section class="abs service" style="left:599px">
  <svg viewBox="0 0 44 42"><g fill="#e23b3b"><ellipse cx="18" cy="7" rx="13" ry="4.5"/><path d="M5 10c0 3 6 5 13 5s13-2 13-5v6c0 3-6 5-13 5S5 19 5 16z"/><path d="M5 20c0 3 6 5 13 5s13-2 13-5v6c0 3-6 5-13 5S5 29 5 26z"/></g><circle cx="34" cy="32" r="6" fill="none" stroke="#e23b3b" stroke-width="3"/><circle cx="34" cy="32" r="1.6" fill="#e23b3b"/></svg>
  <h3>Data Management</h3>
  <p>Praesent sit amet est In dictum dolor<br>eu dictum porttitor enim felis</p>
  <span class="more">LEARN MORE</span>
</section>

<div class="abs divider"></div>

<section class="abs what">
  <h2>WHAT WE DO</h2>
  <p class="lead">Morbi diam mauris viverra in gravida eu mattis in ante Morbi eget arcu Morbi porta libero id ullamcorper nonummy nibh ligula</p>
  <p class="body">Suspendisse vulputate aliquam dui Nulla elementum dui ut augue Aliquam vehicula mi at mauris Maecenas placerat nisl at consequat rhoncus sem nunc gravida justo quis eleifend arcu velit quis lacus Morbi magna magna tincidunt a mattis non imperdiet vitae tellus Sed odio est auctor ac sollicitudin in consequat vitae orci Fusce id</p>
  <p class="label">Our Products:</p>
  <div class="products"><span class="p1">CIVIQ</span><span class="p2">DOCSA</span><span class="p3">ASSETRA</span><span class="p4">PERMITA</span></div>
</section>

<section class="abs recent">
  <h2>Recent Projects</h2>
  <div class="project" style="top:28px">
    <div class="thumb" role="img" aria-label="Photo of staff working at a computer" style="background:linear-gradient(135deg,#3a4150,#9aa2ad)"></div>
    <div><h4>Morbi diam mauris</h4><p>in gravida eu mattis in ante Morbi eget arcu Morbi porta<br>libero id ullamcorper nonummy nibh ligula pulvinar</p></div>
  </div>
  <div class="project" style="top:83px">
    <div class="thumb" role="img" aria-label="Photo of an engineer in a server room" style="background:linear-gradient(135deg,#3c6fb6,#c9d9ef)"></div>
    <div><h4>Vivamus sollicitudin</h4><p>in gravida eu mattis in ante Morbi eget arcu Morbi porta<br>libero id ullamcorper nonummy nibh ligula</p></div>
  </div>
  <div class="project" style="top:139px">
    <div class="thumb" role="img" aria-label="Photo of network cabling in a data center" style="background:linear-gradient(135deg,#1e2c44,#6f8fb3)"></div>
    <div><h4>Curabitur vel mi sit amet</h4><p>gravida eu mattis in ante Morbi eget arcu Morbi porta<br>libero id ullamcorper nonummy nibh ligula</p></div>
  </div>
</section>

<section class="abs certs" aria-label="Certifications">
  <span class="abs row-label" style="left:126px;top:23px">Certifications</span>
  <span class="badge" style="left:231px;top:19px;width:48px;height:28px;background:#1d4f8f;border-color:#1d4f8f"></span>
  <span class="badge" style="left:301px;top:20px;width:54px;height:27px;background:#e8e8ee"></span>
  <span class="badge" style="left:381px;top:19px;width:52px;height:28px;background:#f1dcc8"></span>
  <span class="badge" style="left:455px;top:19px;width:52px;height:28px;background:#efe1c8"></span>
  <span class="badge" style="left:530px;top:19px;width:68px;height:28px;background:#fff;border-color:#3b62a8"></span>
  <span class="badge" style="left:621px;top:20px;width:60px;height:26px;background:#fff;border-color:#999"></span>
  <span class="badge" style="left:704px;top:21px;width:34px;height:25px;background:#f7edc9;border-color:#c8ab5a"></span>
</section>

<section class="abs clients" aria-label="Clients">
  <span class="abs row-label" style="left:131px;top:24px">Clients</span>
  <span class="client" style="left:221px;top:24px;font-size:9px"><i style="width:10px;height:10px;background:#2aa0d8;display:block"></i>BAYWATER</span>
  <span class="badge" style="left:288px;top:20px;width:29px;height:23px;background:#2b5aa8;border:0"></span>
  <span class="badge" style="left:344px;top:20px;width:26px;height:24px;background:#3b5a2e;border:0"></span>
  <span class="badge" style="left:394px;top:21px;width:22px;height:22px;background:#1f7f43;border:0;border-radius:50%"></span>
  <span class="client" style="left:442px;top:28px;font-size:7px;color:#2a4a8a">ELMRIDGE COUNTY</span>
  <span class="badge" style="left:524px;top:20px;width:22px;height:22px;background:#6d9a8f;border:0"></span>
  <span class="badge" style="left:578px;top:20px;width:24px;height:24px;background:#2a3f9a;border:0"></span>
  <span class="badge" style="left:632px;top:20px;width:24px;height:24px;background:#fff;border:3px solid #222;border-radius:50%"></span>
  <span class="client" style="left:676px;top:24px;font-size:12px;color:#222">NORVALE IT</span>
</section>

<footer class="abs footer">
  <div class="fcol" style="left:128px"><h5>COMPANY</h5><ul><li>About Us</li><li>What We Do</li><li>Why Us</li><li>Our Team</li></ul></div>
  <div class="fcol" style="left:242px"><h5>PRODUCTS</h5><ul><li>Proin nulla</li><li>Arcu nonummy</li><li>Luctus dictum</li><li>Eget fermentum</li></ul></div>
  <div class="fcol" style="left:352px"><h5>SERVICES</h5><ul><li>Proin nulla</li><li>Arcu nonummy</li><li>Luctus dictum</li><li>Eget fermentum</li></ul></div>
  <div class="fcol" style="left:459px"><h5>SUPPORT</h5><ul><li>Support</li><li>FAQ</li><li>Resources</li><li>Contact</li></ul></div>
  <div class="fcol" style="left:553px"><h5>SUPPORT</h5><ul><li>Get in touch</li></ul>
    <div class="social" aria-label="Social media links"><i></i><i></i><i></i><i></i></div>
  </div>
</footer>
<div class="abs legal">© 2014 Company Name &nbsp;All right reserved &nbsp;Term of Use</div>

</body>
</html>
```